Business Card Design Project

This is the first time we use our new logo. We need a business card that we can use both on our institutional corporate relationships and also that works for our staff that deals with consumers directly.

VELUNDA is a new company dedicated to empower consumers and to provide them with the best choices for specialized health care using the latest telemedicine technology (medicine at a distance via videoconference).

We want to print this cards in high quality materials and process. We will like designs that allow us to use UV spot varnish and other techniques that will differentiate us.

We are including Two different versions of Color logos. In addition we are including white over black background logos. Those can be used replacing the black for a color.

Please note this is the first time we will be creating any corporate materials with our new logo and colors.

Target Market(s)

34+ consumers of medium high and high socioeconomic levels.

Industry/Entity Type

Health

Requirements
Must have
• Our logo on its original colors
Should not have
• Any other graphical element or design that is not our logo

```html
<!DOCTYPE html>
<html lang="en">
<head>
<meta charset="utf-8">
<title>VELUNDA Business Card</title>
<link rel="stylesheet" href="https://fonts.googleapis.com/css2?family=Montserrat:wght@600;700&family=Arimo:wght@400&display=swap">
<style>
  :root {
    --page: #eceef1;
    --paper: #ffffff;
    --navy: #1a5784;
    --brand-blue: #1f74b9;
    --sky: #5bb3e0;
    --teal: #1aa39a;
    --white: #ffffff;
  }
  html, body {
    margin: 0;
    width: 1200px;
    height: 987px;
    overflow: hidden;
    background: var(--page);
  }
  .canvas {
    width: 1200px;
    height: 987px;
    display: flex;
    flex-direction: column;
    align-items: center;
    justify-content: center;
    gap: 40px;
  }
  .card {
    width: 780px;
    height: 446px;
    border-radius: 24px;
    overflow: hidden;
    box-shadow: 0 6px 18px rgba(0,0,0,0.12);
    display: block;
  }
  .wordmark { font-family: "Montserrat", sans-serif; font-weight: 700; letter-spacing: 3px; }
  .person-name { font-family: "Montserrat", sans-serif; font-weight: 700; }
  .person-title { font-family: "Arimo", sans-serif; }
  .contact { font-family: "Arimo", sans-serif; font-size: 17px; fill: var(--white); }
  .web-line { font-family: "Arimo", sans-serif; font-size: 18px; letter-spacing: 5px; fill: var(--white); }
</style>
</head>
<body>
<main class="canvas">

  <svg class="card card-front" viewBox="0 0 780 446" xmlns="http://www.w3.org/2000/svg" aria-label="Business card front">
    <rect width="780" height="446" fill="var(--paper)"/>
    <path class="accent-swoosh" d="M0,215 C90,300 330,352 560,346 C400,362 150,330 0,262 Z" fill="var(--sky)"/>
    <path class="info-band" d="M0,258 C160,335 420,360 780,300 L780,446 L0,446 Z" fill="var(--navy)"/>

    <g class="brand-lockup">
      <circle cx="62" cy="62" r="18" fill="var(--brand-blue)"/>
      <text class="wordmark" x="96" y="76" font-size="44" fill="var(--navy)">VELUNDA</text>
    </g>

    <text class="person-name" x="60" y="170" font-size="30" fill="var(--navy)">Your Name</text>
    <text class="person-title" x="60" y="194" font-size="18" fill="var(--teal)">Title</text>

    <g class="contact-list" text-anchor="end">
      <text class="contact" x="740" y="352">012-345-6789</text>
      <text class="contact" x="740" y="374">012-345-6789</text>
      <text class="contact" x="740" y="396">name@velunda.com</text>
      <text class="contact" x="740" y="418">www.velunda.com</text>
    </g>
    <g class="contact-icons" fill="none" stroke="var(--white)" stroke-width="1.5">
      <circle cx="617" cy="346" r="6"/>
      <circle cx="617" cy="368" r="6"/>
      <rect x="568" y="385" width="12" height="9" rx="1"/>
      <circle cx="592" cy="412" r="6"/>
    </g>

    <text class="contact address" x="40" y="424">Street Name, City Name, State, City Zip Code</text>
  </svg>

  <svg class="card card-back" viewBox="0 0 780 446" xmlns="http://www.w3.org/2000/svg" aria-label="Business card back">
    <rect width="780" height="446" fill="var(--brand-blue)"/>
    <g class="brand-lockup">
      <circle cx="250" cy="200" r="22" fill="var(--white)"/>
      <text class="wordmark" x="290" y="218" font-size="52" fill="var(--white)">VELUNDA</text>
    </g>
    <text class="web-line" x="390" y="300" text-anchor="middle">www.velunda.com</text>
  </svg>

</main>
</body>
</html>
```